VORLANE (PTY)LTD Website design

WEBSITE design based on our different divisions in our organization.
Our company specializes in the following.
Construction
Property development
Demolition
Mining
Transport
Manufacturing of concrete bricks and blocks
Lightweight concrete Readymix
I want a very modern website and look that fits in with our organization and the changing times of the world.
The website must be very professional and crisp and should appeal to both the younger generation and older generation of business leaders and.
The website must be very user friendly and easy to navigate, simple yet modern, professional and corporate.

```html
<!DOCTYPE html>
<html lang="en">
<head>
<meta charset="utf-8">
<title>VORLANE (PTY)LTD – Building Futures</title>
<link rel="stylesheet" href="https://fonts.googleapis.com/css2?family=Montserrat:wght@400;600;700;800&family=Open+Sans:wght@400;600;700&display=swap">
<style>
:root{
  --blue:#1565c0;
  --blue-mid:#1e77d0;
  --blue-light:#3d95e6;
  --dark:#1b1c1e;
  --ink:#2b2f36;
  --muted:#6c7380;
  --grey:#eeeff1;
  --line:#d8dbe0;
  --white:#ffffff;
}
*{margin:0;padding:0;box-sizing:border-box}
html,body{width:1200px;height:4401px;overflow:hidden}
body{font-family:"Open Sans",Arial,sans-serif;color:var(--ink);background:var(--white);position:relative}
section,header,footer,nav{position:absolute;left:0;width:1200px}
.abs{position:absolute}
.h-title{font-family:"Montserrat",Arial,sans-serif;font-weight:800;font-size:30px;letter-spacing:1px;color:var(--blue);text-transform:uppercase;white-space:nowrap}
.h-title .boxed{display:inline-block;border:2px solid var(--blue);border-bottom-width:4px;padding:0 8px;margin-left:6px;line-height:1.1}
.h-title.light{color:var(--white)}
.h-title.light .boxed{border-color:var(--white)}
.center{left:0;width:1200px;text-align:center}
.btn{position:absolute;background:var(--blue);color:var(--white);font-family:"Montserrat",Arial,sans-serif;font-weight:700;font-size:12px;letter-spacing:.5px;display:flex;align-items:center;justify-content:center;text-transform:uppercase}
.btn.alt{background:var(--blue-light)}
.copy{font-size:12.5px;line-height:1.75;color:var(--muted)}
.ph{position:absolute}
.arrow-box{position:absolute;width:30px;height:30px;background:#5a5f66;display:flex;align-items:center;justify-content:center}
.arrow-box.light{background:rgba(255,255,255,.25)}

/* header */
.topbar{top:0;height:94px;background:var(--white)}
.logo{left:104px;top:26px}
.logo-name{font-family:"Montserrat",Arial,sans-serif;font-weight:800;font-size:38px;color:var(--blue);letter-spacing:1px;line-height:1}
.socials{left:555px;top:40px;display:flex;gap:14px}
.socials span{width:12px;height:12px;border-radius:50%;background:#9aa3ae}
.contact-item{top:37px;display:flex;align-items:center;gap:8px;font-size:12px;color:var(--ink);white-space:nowrap}
.main-nav{top:94px;height:38px;background:var(--blue)}
.main-nav ul{list-style:none;display:flex;position:absolute;left:112px;top:0;height:38px;align-items:center}
.main-nav li{font-family:"Montserrat",Arial,sans-serif;font-weight:700;font-size:12.5px;color:var(--white);text-transform:uppercase;height:38px;display:flex;align-items:center;justify-content:center}
.main-nav li.active{background:var(--blue-light)}

/* hero */
.hero{top:132px;height:534px}
.hero-frame{left:112px;top:172px;width:444px;height:100px;border:4px solid var(--blue);border-right:none}
.hero-title{left:122px;top:190px;font-family:"Montserrat",Arial,sans-serif;font-weight:700;font-size:38px;color:var(--white);letter-spacing:1px}
.hero-list{left:124px;top:246px;font-size:10px;color:#dfe6ee;letter-spacing:1px;display:flex;gap:12px;font-weight:600}
.hero-tag{left:118px;top:296px;font-family:"Montserrat",Arial,sans-serif;font-weight:600;font-size:17px;letter-spacing:12px;color:var(--blue-light)}

/* welcome */
.welcome{top:666px;height:434px}
.video-frame{left:944px;top:58px;width:182px;height:296px;border:6px solid var(--blue);border-left:none}

/* provide */
.provide{top:1100px;height:411px;background:linear-gradient(135deg,#1a6cc2,#1562b3 50%,#1b70c6)}
.service-card{position:absolute;top:122px;width:178px}
.service-card .img{height:202px}
.service-card .label{height:32px;background:var(--blue-light);color:var(--white);font-family:"Montserrat",Arial,sans-serif;font-weight:700;font-size:10.5px;display:flex;align-items:center;justify-content:center;text-transform:uppercase}

/* why */
.why{top:1511px;height:381px;background:var(--grey)}
.feature{position:absolute;top:124px;width:170px;text-align:center}
.feature .icon{width:92px;height:92px;margin:0 auto;background:#111;display:flex;align-items:center;justify-content:center}
.feature .icon.on{background:var(--blue);outline:4px solid #cfd7e3}
.feature h4{font-family:"Montserrat",Arial,sans-serif;font-size:11px;font-weight:700;margin-top:16px;color:var(--ink)}
.feature p{font-size:11px;color:var(--muted)}

/* projects */
.projects{top:1892px;height:499px}
.proj-head{font-family:"Montserrat",Arial,sans-serif;font-weight:700;font-size:16px;color:var(--blue);line-height:1.4;text-transform:uppercase}

/* blogs */
.blogs{top:2391px;height:587px;background:var(--grey)}
.blog{position:absolute;top:120px;width:245px}
.blog .img{height:265px;position:relative}
.blog .date{position:absolute;right:10px;bottom:-10px;width:48px;height:48px;background:rgba(40,40,40,.75);color:var(--white);font-family:"Montserrat",Arial,sans-serif;font-weight:700;font-size:12px;display:flex;align-items:center;justify-content:center}
.blog h5{font-family:"Montserrat",Arial,sans-serif;font-weight:700;font-size:12.5px;line-height:1.45;margin-top:26px;color:var(--ink)}
.blog p{font-size:11px;line-height:1.6;color:var(--muted);margin-top:8px}
.blog .more{font-family:"Montserrat",Arial,sans-serif;font-weight:700;font-size:11px;margin-top:12px;color:var(--ink)}

/* testimonials */
.testimonials{top:2978px;height:352px;background:linear-gradient(135deg,#1a6cc2,#1560b0)}
.quote{position:absolute;top:120px;height:82px;display:flex;gap:14px}
.quote .avatar{width:78px;height:82px;background:#dfe5ec;border:4px solid var(--white)}
.quote .bubble{width:250px;background:var(--white);padding:10px 12px;font-size:10.5px;line-height:1.55;color:var(--muted)}
.quote-name{position:absolute;top:222px;font-family:"Montserrat",Arial,sans-serif;font-weight:700;font-size:12px;color:var(--white);display:flex;gap:14px;align-items:center}
.stars{color:#8fb9e8;letter-spacing:2px;font-size:11px}

/* contact */
.contact{top:3330px;height:396px}
.field{position:absolute;height:40px;background:var(--white);border:1px solid var(--line);box-shadow:0 4px 10px rgba(0,0,0,.08);font-size:11px;color:var(--muted);padding:12px 14px}

/* clients */
.clients{top:3726px;height:249px;background:var(--grey)}
.client{position:absolute;top:160px;font-family:"Montserrat",Arial,sans-serif;font-weight:700;font-size:20px;color:#55595f;display:flex;align-items:center;gap:8px}
.client i{width:12px;height:12px;background:#55595f;display:inline-block}

/* newsletter */
.newsletter{top:3975px;height:103px;background:var(--white)}

/* footer */
.site-footer{top:4078px;height:323px;background:var(--dark);color:#cfd3d8}
.f-head{font-family:"Montserrat",Arial,sans-serif;font-weight:700;font-size:14px;color:var(--white);text-transform:uppercase}
.f-links{list-style:none;font-size:11px;line-height:2.05;color:#bfc4ca;text-transform:uppercase}
.loc{position:absolute;top:80px;width:150px;font-size:10.5px;color:#bfc4ca;line-height:1.6}
.loc b{font-family:"Montserrat",Arial,sans-serif;color:var(--white);font-size:11px;display:flex;align-items:center;gap:6px;margin-bottom:14px;text-transform:uppercase}
.loc .row{display:flex;gap:8px;margin-bottom:12px}
.loc .row strong{color:var(--white);display:block;font-size:10.5px}
.pin{width:10px;height:10px;border-radius:50%;background:var(--blue-light);flex:none;margin-top:3px}
</style>
</head>
<body>

<header class="topbar">
  <div class="abs logo">
    <div class="logo-name">VORLANE</div>
  </div>
  <div class="abs socials"><span></span><span></span><span></span></div>
  <div class="abs contact-item" style="left:660px">
    <svg width="14" height="14" viewBox="0 0 24 24"><path fill="#1565c0" d="M6.6 10.8a15 15 0 0 0 6.6 6.6l2.2-2.2c.3-.3.7-.4 1-.2 1.1.4 2.3.6 3.6.6.6 0 1 .4 1 1V20c0 .6-.4 1-1 1A17 17 0 0 1 3 4c0-.6.4-1 1-1h3.5c.6 0 1 .4 1 1 0 1.3.2 2.5.6 3.6.1.3 0 .7-.2 1z"/></svg>
    +27 (0) 11 555 0142
  </div>
  <div class="abs contact-item" style="left:810px">
    <svg width="16" height="12" viewBox="0 0 16 12"><rect x="1" y="1" width="14" height="10" fill="none" stroke="#1565c0" stroke-width="1.6"/><path d="M1 1l7 6 7-6" fill="none" stroke="#1565c0" stroke-width="1.6"/></svg>
    info@vorlane.co.za
  </div>
  <div class="btn" style="left:968px;top:30px;width:128px;height:32px;font-size:10.5px">Get the quote</div>
</header>

<nav class="main-nav">
  <ul>
    <li class="active" style="width:62px">Home</li>
    <li style="width:120px">About Us</li>
    <li style="width:108px">Service</li>
    <li style="width:118px">Projects</li>
    <li style="width:112px">Careers</li>
    <li style="width:100px">Blogs</li>
    <li style="width:150px">Testimonials</li>
    <li style="width:130px">Contact Us</li>
  </ul>
</nav>

<section class="hero">
  <div class="ph" role="img" aria-label="Excavator working on a demolition site with rubble" style="left:0;top:0;width:1200px;height:534px;background:linear-gradient(100deg,#1c2430 0%,#3a434f 35%,#6b6e70 60%,#4a4538 80%,#2a2c30 100%)"></div>
  <div class="abs hero-frame"></div>
  <div class="abs hero-title">WE ARE SPECIALIZES IN</div>
  <div class="abs hero-list"><span>✓ CONSTRUCTION</span><span>✓ DEMOLITION</span><span>✓ MINING</span><span>✓ TRANSPORT</span><span>✓ PROPERTY DEVELOPMENT</span></div>
  <div class="abs hero-tag">BUILDING FUTURES</div>
  <div class="btn alt" style="left:303px;top:350px;width:142px;height:36px">Contact Now</div>
</section>

<section class="welcome">
  <div class="abs h-title" style="left:210px;top:60px">Welcome <span class="boxed">To Vorlane</span></div>
  <p class="abs copy" style="left:210px;top:108px;width:355px">Our teams plan, build and deliver sites across the region with care for safety, time and cost. We work with clients from first survey to final handover.</p>
  <p class="abs copy" style="left:210px;top:192px;width:355px">From earthworks and demolition to new homes and offices, we bring trained crews, modern plant and firm project control to each job.</p>
  <p class="abs copy" style="left:210px;top:276px;width:355px">We also supply concrete bricks, blocks and readymix from our yards.</p>
  <div class="btn" style="left:210px;top:345px;width:128px;height:34px;font-size:10.5px">Learn More</div>
  <div class="abs video-frame"></div>
  <div class="ph" role="img" aria-label="Video still of construction workers in hard hats and safety vests" style="left:706px;top:76px;width:420px;height:272px;background:linear-gradient(135deg,#9fb6c9,#6c8aa3 45%,#c9a93f 75%,#4e6074)">
    <svg class="abs" style="left:182px;top:108px" width="56" height="56" viewBox="0 0 56 56"><circle cx="28" cy="28" r="26" fill="rgba(255,255,255,.9)"/><path d="M22 17l17 11-17 11z" fill="#1565c0"/></svg>
    <div class="abs" style="left:0;bottom:0;width:420px;height:20px;background:rgba(0,0,0,.55)"></div>
    <div class="abs" style="left:30px;bottom:9px;width:300px;height:3px;background:#8a8f96"></div>
    <div class="abs" style="left:30px;bottom:9px;width:90px;height:3px;background:#e03a3a"></div>
  </div>
</section>

<section class="provide">
  <div class="abs h-title light center" style="top:58px">What We <span class="boxed">Provide</span></div>
  <div class="arrow-box light" style="left:145px;top:228px"><svg width="10" height="12"><path d="M8 1L2 6l6 5" stroke="#fff" stroke-width="2" fill="none"/></svg></div>
  <div class="arrow-box light" style="left:1022px;top:228px"><svg width="10" height="12"><path d="M2 1l6 5-6 5" stroke="#fff" stroke-width="2" fill="none"/></svg></div>
  <div class="service-card" style="left:212px"><div class="img" role="img" aria-label="Construction site with steel frame and crane" style="background:linear-gradient(160deg,#b9c8d6,#8e7d63 55%,#5b4f42)"></div><div class="label">Construction</div></div>
  <div class="service-card" style="left:412px"><div class="img" role="img" aria-label="Two businessmen shaking hands in an office" style="background:linear-gradient(160deg,#dfe3e8,#aab4c0 60%,#6e7c8e)"></div><div class="label">Property Development</div></div>
  <div class="service-card" style="left:612px"><div class="img" role="img" aria-label="Yellow machine on a demolition site" style="background:linear-gradient(160deg,#6a6d70,#3b3d40 50%,#c9a32a)"></div><div class="label">Demolition</div></div>
  <div class="service-card" style="left:810px"><div class="img" role="img" aria-label="Truck driving on a highway at sunset" style="background:linear-gradient(160deg,#e9c27a,#c78a4a 45%,#5b6270)"></div><div class="label">Transport</div></div>
</section>

<section class="why">
  <div class="abs h-title center" style="top:58px">Why Choose <span class="boxed">Vorlane</span></div>
  <div class="feature" style="left:212px">
    <div class="icon"><svg width="46" height="46" viewBox="0 0 46 46" fill="none" stroke="#fff" stroke-width="2.5"><rect x="5" y="9" width="36" height="28"/><path d="M5 17h36M13 25h10M13 30h14"/><circle cx="33" cy="28" r="4"/></svg></div>
    <h4>25 YEAR OF</h4><p>EXPERIENCE</p>
  </div>
  <div class="feature" style="left:415px">
    <div class="icon on"><svg width="46" height="46" viewBox="0 0 46 46" fill="none" stroke="#fff" stroke-width="2.5"><circle cx="23" cy="15" r="7"/><path d="M10 40c0-8 6-13 13-13s13 5 13 13"/><path d="M14 13h18"/></svg></div>
    <h4>PROFESSIONAL &amp;</h4><p>RESPONSIBLE</p>
  </div>
  <div class="feature" style="left:614px">
    <div class="icon"><svg width="46" height="46" viewBox="0 0 46 46" fill="none" stroke="#fff" stroke-width="2.5"><circle cx="23" cy="23" r="7"/><path d="M23 5v7M23 34v7M5 23h7M34 23h7M10 10l5 5M31 31l5 5M36 10l-5 5M15 31l-5 5"/></svg></div>
    <h4>FAST &amp; EFFECTIVE</h4><p>SERVICE</p>
  </div>
  <div class="feature" style="left:815px">
    <div class="icon"><svg width="46" height="46" viewBox="0 0 46 46" fill="none" stroke="#fff" stroke-width="2.5"><circle cx="23" cy="19" r="12"/><path d="M16 29l-3 12 10-5 10 5-3-12"/><path d="M18 19l4 4 6-7"/></svg></div>
    <h4>100% SATISFACTION</h4><p>GUARANTEE</p>
  </div>
  <div class="btn" style="left:538px;top:290px;width:124px;height:34px;font-size:10.5px">Contact Now</div>
</section>

<section class="projects">
  <div class="abs h-title center" style="top:58px">Our <span class="boxed">Projects</span></div>
  <div class="abs" style="left:0;top:122px;width:300px;height:280px;background:var(--blue)"></div>
  <div class="ph" role="img" aria-label="Close-up of rough concrete and stone texture" style="left:0;top:162px;width:225px;height:245px;background:linear-gradient(135deg,#6d7176,#a4a7ab 50%,#585c61);border:6px solid #fff"></div>
  <div class="ph" role="img" aria-label="Two engineers in safety vests on an open site" style="left:238px;top:160px;width:330px;height:250px;background:linear-gradient(170deg,#a9c6e2,#d7dbdf 45%,#c9b78a 70%,#9c8a62);border:6px solid #fff;box-shadow:0 6px 16px rgba(0,0,0,.15)"></div>
  <div class="arrow-box" style="left:362px;top:425px;width:26px;height:26px;background:#d6d9dd"><svg width="8" height="10"><path d="M7 1L2 5l5 4" stroke="#555" stroke-width="1.8" fill="none"/></svg></div>
  <div class="arrow-box" style="left:402px;top:425px;width:26px;height:26px;background:#d6d9dd"><svg width="8" height="10"><path d="M1 1l5 4-5 4" stroke="#555" stroke-width="1.8" fill="none"/></svg></div>
  <div class="abs proj-head" style="left:607px;top:160px;width:390px">Building landmark sites with trusted teams and solid results.</div>
  <p class="abs copy" style="left:607px;top:218px;width:385px">Each project is planned in detail, staffed with skilled crews and run to a clear schedule. We report progress openly so clients always know where work stands.</p>
  <p class="abs copy" style="left:607px;top:298px;width:385px">See the sites, estates and roads our people have delivered over the years.</p>
  <div class="btn" style="left:607px;top:356px;width:145px;height:32px;font-size:10.5px">View All Projects</div>
  <div class="ph" role="img" aria-label="Smiling builder in a hard hat and tool belt giving a thumbs up" style="left:1000px;top:100px;width:172px;height:399px;background:linear-gradient(180deg,#f2b632 0%,#f2b632 10%,#2a63b8 35%,#1f4f99 65%,#8a6a3c 100%);border-radius:60px 60px 0 0"></div>
</section>

<section class="blogs">
  <div class="abs h-title center" style="top:58px">Our <span class="boxed">Blogs</span></div>
  <div class="arrow-box" style="left:142px;top:240px"><svg width="10" height="12"><path d="M8 1L2 6l6 5" stroke="#fff" stroke-width="2" fill="none"/></svg></div>
  <div class="arrow-box" style="left:1025px;top:240px"><svg width="10" height="12"><path d="M2 1l6 5-6 5" stroke="#fff" stroke-width="2" fill="none"/></svg></div>
  <div class="blog" style="left:210px">
    <div class="img" role="img" aria-label="Site foreman reviewing plans outdoors" style="background:linear-gradient(160deg,#cfd8e0,#8e8a80 55%,#5c5a55)"><div class="date">DEC</div></div>
    <h5>New safety rules on our sites this season, read more here.</h5>
    <p>Short notes on training, gear and daily checks our crews now follow on site.</p>
    <div class="more">LEARN MORE</div>
  </div>
  <div class="blog" style="left:477px">
    <div class="img" role="img" aria-label="Workers in yellow vests and hard hats on site" style="background:linear-gradient(160deg,#bfc8d0,#d8cf5a 50%,#6e7478)"><div class="date">OCT</div></div>
    <h5>How we plan a build from survey to final handover.</h5>
    <p>A look at the stages, checks and people behind every project we deliver.</p>
    <div class="more" style="color:var(--blue)">LEARN MORE</div>
  </div>
  <div class="blog" style="left:745px">
    <div class="img" role="img" aria-label="Worker tying steel rebar on a slab" style="background:linear-gradient(160deg,#8a7a66,#5a4d40 55%,#3a332c)"><div class="date">NOV</div></div>
    <h5>Why quality concrete blocks matter for strong walls.</h5>
    <p>What goes into our bricks and blocks and how we test every batch we make.</p>
    <div class="more">LEARN MORE</div>
  </div>
</section>

<section class="testimonials">
  <div class="abs h-title light center" style="top:58px">Client <span class="boxed">Testimonials</span></div>
  <div class="quote" style="left:245px">
    <div class="avatar" role="img" aria-label="Client portrait"></div>
    <div class="bubble">The team kept us informed at every stage and finished our offices on time and within budget. We would gladly work with them again.</div>
  </div>
  <div class="quote" style="left:612px">
    <div class="avatar" role="img" aria-label="Client portrait"></div>
    <div class="bubble">Clean site, skilled crews and solid results. Their readymix and blocks were delivered exactly when we needed them.</div>
  </div>
  <div class="quote-name" style="left:245px">JASON PIKE <span class="stars">★★★★★</span></div>
  <div class="quote-name" style="left:612px">DANIEL MOSS <span class="stars">★★★★★</span></div>
  <div class="btn alt" style="left:528px;top:270px;width:144px;height:30px;font-size:10px">View All Review</div>
</section>

<section class="contact">
  <div class="ph" role="img" aria-label="Two engineers in hard hats pointing across a site" style="left:0;top:0;width:445px;height:396px;background:linear-gradient(90deg,#c9cfd4 0%,#e4d56a 40%,#d8dde2 80%,rgba(255,255,255,0) 100%)"></div>
  <div class="abs h-title" style="left:470px;top:58px;width:300px;text-align:center">Contact <span class="boxed">Us</span></div>
  <div class="field" style="left:465px;top:112px;width:255px">Name</div>
  <div class="field" style="left:735px;top:112px;width:255px">Phone</div>
  <div class="field" style="left:465px;top:160px;width:255px">Email</div>
  <div class="field" style="left:735px;top:160px;width:255px">Service <span style="float:right">▾</span></div>
  <div class="field" style="left:465px;top:208px;width:525px;height:90px">Message</div>
  <div class="btn" style="left:465px;top:312px;width:142px;height:36px;font-size:10.5px">Submit Now</div>
</section>

<section class="clients">
  <div class="abs h-title center" style="top:58px">Our <span class="boxed">Clients</span></div>
  <div class="client" style="left:232px"><i></i>Brantley</div>
  <div class="client" style="left:378px">Northmind</div>
  <div class="abs" style="left:532px;top:140px;width:130px;height:62px;background:#fff;box-shadow:0 3px 10px rgba(0,0,0,.08)"></div>
  <div class="client" style="left:554px">Velique</div>
  <div class="client" style="left:702px"><i></i>Upward</div>
  <div class="client" style="left:864px"><i></i>Stonegate</div>
</section>

<section class="newsletter">
  <div class="ph" role="img" aria-label="Hard hat and hand tools on a bench" style="left:0;top:10px;width:175px;height:70px;background:linear-gradient(90deg,#e0b03a,#b9bec4 60%,#fff)"></div>
  <div class="abs" style="left:212px;top:30px;font-family:'Montserrat',Arial,sans-serif;font-weight:800;font-size:15px;color:var(--blue)">SUBSCRIBE NEWSLETTERS</div>
  <div class="abs copy" style="left:212px;top:50px;width:360px;font-size:11px;line-height:1.5">Get our latest project news, tips and updates sent straight to your inbox each month.</div>
  <div class="field" style="left:615px;top:32px;width:290px;height:38px;font-size:10px">ENTER YOUR EMAIL ADDRESS</div>
  <div class="btn" style="left:922px;top:32px;width:64px;height:38px"><svg width="18" height="16" viewBox="0 0 18 16"><path d="M1 8l16-7-5 14-3-6z" fill="#fff"/></svg></div>
</section>

<footer class="site-footer">
  <div class="abs f-head" style="left:108px;top:40px">Follow Us</div>
  <div class="abs" style="left:108px;top:94px">
    <div class="logo-name" style="font-size:26px;color:#fff">VORLANE</div>
  </div>
  <div class="abs" style="left:108px;top:148px;display:flex;gap:8px">
    <span style="width:22px;height:22px;border:1px solid #888"></span><span style="width:22px;height:22px;border:1px solid #888"></span><span style="width:22px;height:22px;border:1px solid #888"></span>
  </div>
  <div class="abs f-head" style="left:310px;top:40px">Quick Links</div>
  <ul class="abs f-links" style="left:310px;top:72px">
    <li>Home</li><li>About Us</li><li>Service</li><li>Projects</li><li>Careers</li><li>Blogs</li><li>Contact Us</li>
  </ul>
  <div class="abs f-head" style="left:490px;top:40px">Contact Details</div>
  <div class="loc" style="left:490px"><b><span class="pin"></span>Western Cape</b>
    <div class="row"><span class="pin"></span><div><strong>PHONE</strong>+27 (0) 21 555 0181</div></div>
    <div class="row"><span class="pin"></span><div><strong>EMAIL</strong>wc@vorlane.co.za</div></div></div>
  <div class="loc" style="left:645px"><b><span class="pin"></span>Eastern Cape</b>
    <div class="row"><span class="pin"></span><div><strong>PHONE</strong>+27 (0) 41 555 0127</div></div>
    <div class="row"><span class="pin"></span><div><strong>EMAIL</strong>ec@vorlane.co.za</div></div></div>
  <div class="loc" style="left:800px"><b><span class="pin"></span>KZN</b>
    <div class="row"><span class="pin"></span><div><strong>PHONE</strong>+27 (0) 31 555 0163</div></div>
    <div class="row"><span class="pin"></span><div><strong>EMAIL</strong>kzn@vorlane.co.za</div></div></div>
  <div class="loc" style="left:955px"><b><span class="pin"></span>South Africa</b>
    <div class="row"><span class="pin"></span><div><strong>PHONE</strong>+27 (0) 11 555 0142</div></div>
    <div class="row"><span class="pin"></span><div><strong>EMAIL</strong>info@vorlane.co.za</div></div></div>
  <div class="abs" style="left:0;top:282px;width:1200px;height:1px;background:#333"></div>
  <div class="abs" style="left:108px;top:296px;font-size:10px;color:#8d939a">© COPYRIGHT 2024 VORLANE (PTY)LTD. ALL RIGHTS RESERVED.</div>
  <div class="abs" style="left:1010px;top:296px;font-size:10px;color:#8d939a">PRIVACY · POLICY</div>
</footer>

</body>
</html>
```